Homepage design for female-owned English/French speaking Law firm

Brief Update - we prefer not to have a photo of a person in the hero shot

Corvell.com.au is the website for a English/French Bilingual Female-owned Law Firm, Morillaqua Corvell.
Overall Design notes:
Professional, yet warm and welcoming
Historic foundations but Progressive, woman-owned, sleek, innovative and modern.
Approachable, casual yet professional. Sans-serif font and light colours would help this
2 languages switched by flags (English/French)

Winner must provide
Home page design
Standard (inner) page design (can be provided after winner is selected)
All photos used in the design without charge
Updates

Requirements
Should not have
• Update - we prefer not to have a photo of a person in the hero shot

```html
<!DOCTYPE html>
<html lang="en">
<head>
<meta charset="utf-8">
<title>Morillaqua Corvell Solicitors</title>
<link href="https://fonts.googleapis.com/css2?family=Inter:wght@400;500;600;700&display=swap" rel="stylesheet">
<style>
:root{
  --orange:#f7862a;
  --ink:#2b2b2b;
  --muted:#555;
  --page:#f9f6f2;
  --hero:#ece6df;
  --white:#fff;
  --line:#c9c4be;
}
*{box-sizing:border-box;margin:0;padding:0}
html,body{width:1200px;height:3002px;overflow:hidden}
body{font-family:"Inter",sans-serif;background:var(--page);color:var(--ink);position:relative}
.abs{position:absolute}
/* top bar */
.topbar{left:66px;top:0;width:1067px;height:37px;border-bottom:1px solid #d8d2cb;display:flex;align-items:center;font-size:11px;color:#444;gap:26px}
.topbar span{display:flex;align-items:center;gap:7px}
.lang{margin-left:auto;display:flex;align-items:center;gap:6px}
.logo{font-weight:400;color:var(--orange);letter-spacing:-.3px}
.logo small{display:block;font-size:8.5px;letter-spacing:2.2px;color:#555;margin-top:2px}
.nav{top:56px;left:66px;width:1067px;height:42px;display:flex;align-items:center}
.nav .logo{font-size:20px}
.menu{margin-left:auto;display:flex;align-items:center;gap:27px;font-size:14px;font-weight:500;color:#333}
.menu .on{color:var(--orange)}
.btn{display:inline-flex;align-items:center;justify-content:center;background:var(--orange);color:#fff;font-weight:600;font-size:13.5px;height:42px}
.btn.ghost{background:none;border:1.5px solid var(--orange);color:var(--orange)}
/* hero */
.hero{left:0;top:0;width:1200px;height:720px;background:var(--hero);overflow:hidden}
.hero-art{right:0;top:0;width:760px;height:720px;background:radial-gradient(ellipse at 70% 35%,#a99079 0%,#c7b4a1 35%,#e2d8ce 70%,var(--hero) 100%)}
.hero h1{left:66px;top:196px;font-size:68px;line-height:77px;font-weight:600;letter-spacing:.5px;color:var(--ink)}
.hero h1 em{font-style:normal;color:var(--orange)}
.hero p{left:66px;top:452px;width:600px;font-size:13.5px;line-height:21px;color:#444}
/* section heads */
.head{text-align:center;width:1200px;left:0}
.head h2{font-size:42px;font-weight:500;letter-spacing:.5px}
.head h2 em{font-style:normal;color:var(--orange)}
.head p{font-size:13.5px;color:#555;margin-top:12px;line-height:21px}
.bar{display:block;width:23px;height:6px;background:#777;margin:14px auto 0}
/* services */
.cards{left:66px;top:911px;width:1067px;display:grid;grid-template-columns:repeat(4,254px);gap:17px 17px}
.card{background:var(--white);height:199px;display:flex;flex-direction:column;align-items:center;justify-content:center;text-align:center;font-size:13.5px;font-weight:600;line-height:16px;color:#333}
.card svg{margin-bottom:18px}
.card.active{border:2px solid var(--orange)}
/* about */
.about-bg{left:0;top:1375px;width:1200px;height:483px;background:linear-gradient(180deg,#f3eee9 0%,#e8ddd2 55%,#c9b9a6 100%)}
.about ul{list-style:none;left:250px;width:700px;top:1522px;text-align:center;font-size:13.5px;line-height:21px;color:#333}
.about li{margin-bottom:21px}
.about li::before{content:"• "}
.stats{left:66px;top:1780px;width:1067px;height:157px;background:var(--white);display:flex;align-items:center}
.stat{flex:1;text-align:center;position:relative}
.stat+.stat::before{content:"";position:absolute;left:0;top:22px;width:2px;height:46px;background:var(--line)}
.stat span{font-size:13.5px;color:#333}
.stat b{display:block;font-size:44px;font-weight:600;color:var(--orange);margin-top:8px;letter-spacing:1px}
/* contact */
.contact-bg{left:0;top:2000px;width:600px;height:537px;background:linear-gradient(180deg,#f1ece6 0%,#ddd3c8 50%,#b9ab9b 100%)}
.contact-bg2{left:600px;top:2000px;width:600px;height:537px;background:var(--white)}
.touch{left:0;top:2050px;width:600px;text-align:center}
.info{font-size:13.5px;line-height:27px;color:#222}
.form{left:642px;top:2018px;width:452px;font-size:13.5px}
.form label{display:block;font-weight:600;margin-bottom:12px}
.form label i{color:#e22;font-style:normal}
.field{border:1px solid #999;border-radius:4px;height:42px;padding:0 16px;display:flex;align-items:center;color:#888;font-size:13px;margin-bottom:12px}
/* footer */
.footer{left:0;top:2537px;width:1200px;height:465px}
.fcol{font-size:13.5px;color:#333}
.fcol h4{color:var(--orange);font-size:16.5px;font-weight:500;margin-bottom:17px}
.fcol a{display:block;margin-bottom:19px;color:#333;text-decoration:none}
</style>
</head>
<body>

<section class="hero abs">
  <div class="hero-art abs" role="img" aria-label="Bronze statue of Lady Justice holding scales, softly faded"></div>
  <svg class="abs" style="left:0;top:0" width="1200" height="720"><path d="M1200 390 Q1185 690 880 720 L1200 720 Z" fill="var(--page)"/></svg>
  <h1 class="abs">WE ARE A <em>FIRM OF<br>FRENCH-SPEAKING</em><br>LAWYERS</h1>
  <p class="abs">located in the Sydney central business district. We provide a broad range of legal services in English and French to clients in Australia and overseas.</p>
  <a class="btn abs" style="left:66px;top:544px;width:200px">Appointment now</a>
  <a class="btn ghost abs" style="left:293px;top:544px;width:200px">Lean more</a>
</section>

<div class="topbar abs">
  <span><svg width="11" height="9"><rect x=".5" y=".5" width="10" height="8" fill="#666"/><path d="M.5 .5 L5.5 5 L10.5 .5" stroke="#fff" fill="none"/></svg>clara@corvell.com.au</span>
  <span><svg width="11" height="11"><path d="M2 1 L4 1 L5 4 L3.5 5 Q5 7.5 7 8.5 L8 7 L11 8 L11 10 Q5 11 1 3 Z" fill="#666"/></svg>(+612) 9000 1234</span>
  <span><svg width="11" height="11"><circle cx="5.5" cy="5.5" r="4.5" fill="none" stroke="#666" stroke-width="2" stroke-dasharray="2 1.5"/></svg>Migration Agent's registration No : 1048215</span>
  <span class="lang"><svg width="27" height="18"><rect width="9" height="18" fill="#2a3fbf"/><rect x="9" width="9" height="18" fill="#fff"/><rect x="18" width="9" height="18" fill="#e3262b"/></svg><svg width="10" height="6"><path d="M1 1 L5 5 L9 1" stroke="#333" stroke-width="1.5" fill="none"/></svg></span>
</div>

<nav class="nav abs">
  <div class="logo">morillaqua corvell solicitors<small>Avocats Francophones - French Speaking Lawyers</small></div>
  <div class="menu">
    <span class="on">Home</span><span>About us</span>
    <span>Our service <svg width="10" height="6"><path d="M1 1 L5 5 L9 1" stroke="#333" stroke-width="1.5" fill="none"/></svg></span>
    <span>Download &amp; Link</span>
    <a class="btn" style="width:137px">Contact us</a>
  </div>
</nav>

<section class="services">
  <div class="head abs" style="top:768px">
    <h2>OUR <em>SERVICES</em></h2>
    <p>If you have a question relating to other areas of law, please do not hesitate to contact us for referral to an expert in the relevant field.</p>
    <span class="bar"></span>
  </div>
  <div class="cards abs">
    <div class="card active"><svg width="56" height="56" fill="none" stroke="var(--orange)" stroke-width="2"><path d="M4 26 L28 6 L52 26"/><path d="M10 22 V52 H46 V22"/><rect x="22" y="34" width="12" height="18"/><rect x="36" y="32" width="8" height="8"/><rect x="8" y="2" width="22" height="10"/></svg>Property Law including<br>Conveyancing &amp; Leases.</div>
    <div class="card"><svg width="56" height="50" fill="none" stroke="#777" stroke-width="2"><rect x="2" y="12" width="52" height="36"/><path d="M20 12 V4 H36 V12"/><path d="M2 28 H54" stroke-dasharray="6 4"/></svg>Sale &amp; Purchase of<br>Business.</div>
    <div class="card"><svg width="40" height="50" fill="none" stroke="#777" stroke-width="2"><path d="M2 2 H28 L38 12 V48 H2 Z"/><path d="M9 26 H31 M9 32 H31 M9 38 H31"/></svg>Deceased Estates &amp;<br>Wills.</div>
    <div class="card"><svg width="54" height="52" fill="none" stroke="#777" stroke-width="2"><path d="M2 8 L26 2 V50 L2 44 Z"/><path d="M26 8 H50 V44 H26" fill="#777"/><text x="31" y="38" font-size="22" font-weight="700" fill="#fff" stroke="none">A</text><text x="8" y="32" font-size="14" fill="#777" stroke="none">文</text></svg>Translation service.</div>
    <div class="card"><svg width="56" height="50" fill="none" stroke="#777" stroke-width="2"><rect x="2" y="2" width="42" height="30"/><path d="M8 10 H38 M8 17 H38 M8 24 H30"/><path d="M14 32 V40 H40 L48 48 V40 H54 V14 H44"/></svg>Advice in relation to<br>transactions in France.</div>
    <div class="card"><svg width="56" height="52" fill="none" stroke="#777" stroke-width="2"><path d="M2 2 V50 H54"/><path d="M10 40 L18 20 L24 30 L32 14 L38 26 L46 18" /><path d="M10 34 L22 38 L34 30 L48 34"/></svg>Affairs Management.</div>
    <div class="card"><svg width="30" height="52" fill="#777"><circle cx="12" cy="6" r="5"/><path d="M6 14 H18 L22 30 H18 V50 H14 V34 H10 V50 H6 Z"/><rect x="23" y="24" width="3" height="26"/></svg>Elder Law.</div>
    <div class="card"><svg width="40" height="50" fill="#777"><circle cx="12" cy="5" r="4"/><path d="M6 11 H18 V30 H15 V48 H9 V30 H6 Z"/><path d="M22 20 H38 M30 14 V34" stroke="#777" stroke-width="2"/><path d="M20 28 L24 20 L28 28 Z M32 30 L36 22 L40 30 Z"/></svg>Powers of Attorney /<br>Guardianship.</div>
  </div>
</section>

<section class="about">
  <div class="about-bg abs" role="img" aria-label="Sydney harbour with the opera house in warm haze"></div>
  <div class="head abs" style="top:1425px"><h2>ABOUT <em>US</em></h2><span class="bar"></span></div>
  <ul class="abs">
    <li>Our small, skilled team is committed to the delivery of quality legal services to our clients.</li>
    <li>Morillaqua Corvell originated with the legal practice founded by Mr Lucien Marcel Auguste Morillaqua in the 1930s. Today, we are a progressive law firm that has embraced both the traditional approach of our predecessor firms and the efficiencies of modern technology.</li>
    <li>All of our services are available in English or in French according to the needs of our clients.</li>
  </ul>
  <a class="btn abs" style="left:500px;top:1698px;width:200px">Learn more</a>
  <div class="stats abs">
    <div class="stat"><span>Founded in</span><b>1930s</b></div>
    <div class="stat"><span>Trusted customer</span><b>5000+</b></div>
    <div class="stat"><span>Successful Case</span><b>4560+</b></div>
    <div class="stat"><span>Case Closed</span><b>3500+</b></div>
  </div>
</section>

<section class="contact">
  <div class="contact-bg abs" role="img" aria-label="Sydney opera house steps in soft light"></div>
  <div class="contact-bg2 abs"></div>
  <div class="touch abs head" style="width:600px">
    <h2>GET IN <em>TOUCH</em></h2>
    <p>Looking for good lawyer? , Don't be shy.<br>Let's work together.</p>
    <span class="bar"></span>
  </div>
  <div class="info abs" style="left:66px;top:2214px">Level 9, 48 Harlow street<br>Sydney, NSW 2000<br>Australia</div>
  <div class="info abs" style="left:350px;top:2208px;line-height:31px">
    <div>☏&nbsp; Phone: (+612) 9000 1234</div>
    <div>▣&nbsp; Fax: (+612) 9000 1235</div>
    <div>✉&nbsp; E-mail: clara@corvell.com.au</div>
  </div>
  <div class="form abs">
    <label>Full name <i>*</i></label><div class="field">Full name</div>
    <label>Email <i>*</i></label><div class="field">Youremail@address.com</div>
    <label>Phone number</label><div class="field" style="width:311px">Phone number</div>
    <label>Message <i>*</i></label><div class="field" style="height:154px;align-items:flex-start;padding-top:12px;margin-bottom:28px">How we can help you?</div>
    <a class="btn" style="width:200px">Send</a>
  </div>
</section>

<footer class="footer abs">
  <div class="logo abs" style="left:66px;top:62px;font-size:27px">morillaqua corvell solicitors<small style="font-size:10.5px;margin-top:4px">Avocats Francophones - French Speaking Lawyers</small></div>
  <p class="abs" style="left:66px;top:160px;width:340px;font-size:13.5px;line-height:21px;color:#333">Lorem ipsum dolor sit amet consectetur. Elit vitae fringilla quisque dictum cras urna lacus tristique et.</p>
  <div class="fcol abs" style="left:518px;top:75px"><h4>Get to know us</h4><a>Home</a><a>About us</a><a>Download &amp; Link</a></div>
  <div class="fcol abs" style="left:698px;top:75px"><h4>Our service</h4><a>Property law</a><a>Sale of Business</a><a>Wills &amp; Estates</a><a>Translation</a><a>Elder Law</a><a>Powers of Attorney</a><a>French advice</a><a>Affairs management</a></div>
  <div class="fcol abs" style="left:879px;top:75px;line-height:16px"><h4>Contact us</h4><a>Level 9, 48 Harlow street<br>Sydney, NSW 2000<br>Australia</a><a>Phone: (+612) 9000 1234</a><a>Fax: (+612) 9000 1235</a><a>E-mail: clara@corvell.com.au</a></div>
  <p class="abs" style="left:66px;top:420px;font-size:11px;color:#555">2024 © Copyright, morillaqua corvell. All rights reserved.</p>
</footer>

</body>
</html>
```